コンセプトや情報は添付ファイルに書いてますので、それを基に作成お願いします

【注意事項】

※尚、キャバクラやバーにもpopを置くので高級かつ洗練されたデザインを意識してください。

※カラーやフォントの指定はありませんが、いわゆるポスター作成ソフト等によくあるテンプレートを使ったデザインはあまり好ましくありません

※急ぎですので、レスポンスよく返せる方を希望します。

※写真等は何もないのですが、月末には写真素材が届きます。写真素材を使うデザインの場合取り急ぎ、別の素材で代用してください
ロゴのaiデータです

秀逸です

ありがとうございます

```html
<!DOCTYPE html>
<html lang="ja">
<head>
<meta charset="utf-8">
<title>KAGARI 新感覚の高級焼肉bar</title>
<link rel="stylesheet" href="https://fonts.googleapis.com/css2?family=Shippori+Mincho:wght@500;700;800&family=Cormorant+Garamond:wght@500;600;700&display=swap">
<style>
:root{
  --ink:#0c0907;
  --ink-soft:#1d1610;
  --gold:#d3ae63;
  --gold-light:#f3dc9c;
  --gold-deep:#8d6a2c;
  --white:#f4efe6;
  --meat-dark:#5a0f12;
  --meat:#a3262b;
  --meat-light:#d9777a;
}
*{margin:0;padding:0;box-sizing:border-box}
html,body{width:848px;height:1200px;overflow:hidden;background:var(--ink)}
.poster{
  position:relative;width:848px;height:1200px;overflow:hidden;
  background:
    radial-gradient(circle at 12% 18%, rgba(190,130,60,.35) 0 40px, transparent 90px),
    radial-gradient(circle at 28% 30%, rgba(150,95,40,.25) 0 30px, transparent 80px),
    radial-gradient(circle at 8% 48%, rgba(170,110,50,.22) 0 36px, transparent 90px),
    radial-gradient(circle at 90% 55%, rgba(120,70,30,.18) 0 40px, transparent 110px),
    linear-gradient(180deg,#241a11 0%,#130e0a 45%,var(--ink) 100%);
  font-family:"Shippori Mincho",serif;color:var(--white);
}
.gold-text{
  background:linear-gradient(180deg,var(--gold-light) 0%,var(--gold) 55%,var(--gold-deep) 100%);
  -webkit-background-clip:text;background-clip:text;color:transparent;
}
.headline{
  position:absolute;top:40px;left:0;width:100%;text-align:center;
  font-size:50px;font-weight:700;letter-spacing:2px;
}
.photo-meat-top{
  position:absolute;left:537px;top:150px;width:311px;height:262px;
  background:radial-gradient(ellipse at 55% 45%,var(--meat-light) 0%,var(--meat) 40%,var(--meat-dark) 75%,var(--ink) 100%);
}
.brand-panel{
  position:absolute;left:311px;top:147px;width:226px;height:254px;
  background:linear-gradient(135deg,#f6e2a4 0%,#c99b4c 40%,#e9cd86 62%,#9e7634 100%);
  box-shadow:0 10px 30px rgba(0,0,0,.6);
  display:flex;flex-direction:column;align-items:center;justify-content:center;gap:14px;
}
.brand-dot{width:46px;height:46px;border-radius:50%;background:var(--ink-soft)}
.brand-name{font-family:"Cormorant Garamond",serif;font-weight:600;font-size:30px;letter-spacing:6px;color:var(--ink-soft)}
.concept{
  position:absolute;top:446px;left:0;width:100%;text-align:center;
  font-size:15px;letter-spacing:.5px;color:var(--white);
}
.tagline{
  position:absolute;top:482px;left:0;width:100%;text-align:center;
  font-size:31px;font-weight:800;letter-spacing:2px;
}
.opening{
  position:absolute;top:548px;left:92px;display:flex;align-items:flex-end;
  font-family:"Cormorant Garamond",serif;font-weight:600;line-height:1;
}
.opening-date{font-size:138px;letter-spacing:-2px}
.opening-day{font-size:40px;margin:0 26px 20px 10px;font-weight:700}
.opening-word{font-size:132px;letter-spacing:2px}
.hours{
  position:absolute;top:690px;left:438px;font-size:27px;font-weight:700;letter-spacing:1px;
}
.hours span{display:block;line-height:1.6}
.photo-meat-bottom{
  position:absolute;left:0;top:730px;width:430px;height:335px;
  background:radial-gradient(ellipse at 45% 50%,var(--meat-light) 0%,var(--meat) 35%,var(--meat-dark) 68%,transparent 92%);
}
.map{
  position:absolute;left:551px;top:790px;width:212px;height:140px;
  background:linear-gradient(135deg,#2a231c,#3a3128);
}
.footer{
  position:absolute;left:0;top:1069px;width:100%;height:131px;
  background:linear-gradient(180deg,#0a0806,#000);
  border-top:1px solid rgba(211,174,99,.35);
}
.reserve{
  position:absolute;left:16px;top:1094px;width:56px;height:56px;
  border:1px solid var(--white);font-size:12px;line-height:1.35;
  display:flex;align-items:center;justify-content:center;text-align:center;
}
.tel{
  position:absolute;left:86px;top:1086px;font-size:46px;font-weight:700;letter-spacing:1px;
  display:flex;align-items:baseline;gap:4px;
}
.tel small{font-size:30px}
.address{
  position:absolute;left:578px;top:1098px;width:180px;font-size:11px;line-height:1.5;color:var(--white);
}
.qr{
  position:absolute;left:772px;top:1088px;width:62px;height:62px;background:var(--white);
}
</style>
</head>
<body>
<div class="poster">
  <h1 class="headline gold-text">新感覚の高級焼肉bar</h1>

  <div class="photo-meat-top" role="img" aria-label="霜降り牛肉のクローズアップ写真"></div>

  <div class="brand-panel">
    <div class="brand-dot"></div>
    <div class="brand-name">KAGARI</div>
  </div>

  <p class="concept">お洒落なバーカウンター、くつろぎのボックス席、カラオケも楽しむVIPルーム。</p>
  <p class="tagline gold-text">楽しみ方はあなた次第!!</p>

  <div class="opening gold-text">
    <span class="opening-date gold-text">7.5</span>
    <span class="opening-day gold-text">SUN</span>
    <span class="opening-word gold-text">OPEN</span>
  </div>

  <div class="hours gold-text">
    <span class="gold-text">PM 6:00 ~ AM 5:00</span>
    <span class="gold-text">日曜定休</span>
  </div>

  <div class="photo-meat-bottom" role="img" aria-label="皿に盛られた霜降り焼肉用の牛肉の写真"></div>

  <div class="map" role="img" aria-label="店舗周辺の案内地図"></div>

  <footer class="footer"></footer>
  <div class="reserve">ご予約は<br>こちら</div>
  <div class="tel gold-text"><small class="gold-text">tel.</small>052-000-4829</div>
  <p class="address">愛知県名古屋市中区星見町<br>1-2-3 月灯ビル 2F</p>
  <div class="qr"></div>
</div>
</body>
</html>
```